Newsletter template

I am looking for 2 newsletter templates. My website is in Wordpress and I want to use in mailchimp for lists.

One newsletter is for local clients of design remodeling firm to be sent monthly

Second newsletter is for web store offerings to be sent weekly.

Target Market(s)

Luxury home and leisure

Industry/Entity Type

Store

Requirements
Must have
• Use logos and colors to seamlessly integrate with website,

```html
<!DOCTYPE html>
<html lang="en">
<head>
<meta charset="utf-8">
<title>Ellery Rose Fine Living — Weekly Newsletter</title>
<link rel="stylesheet" href="https://fonts.googleapis.com/css2?family=Montserrat:wght@400;600;700;800&family=Open+Sans:wght@400;600&family=Oswald:wght@500;600&family=Raleway:wght@200;300;700&display=swap">
<style>
:root{
  --teal:#16a6c0;
  --lime:#8dc63f;
  --pink:#f2555e;
  --red:#e2262e;
  --mustard:#d9be3a;
  --ink:#2c2c2c;
  --slate:#4c5b6d;
  --grey-text:#6b6b6b;
  --rule:#c9c9c9;
  --footer-bg:#eeeeee;
  --link:#5b9bd8;
  --social:#5fc6ea;
  --white:#ffffff;
}
*{box-sizing:border-box;margin:0;padding:0}
html,body{width:1200px;height:2951px;overflow:hidden;background:var(--white)}
body{font-family:"Montserrat",sans-serif;color:var(--ink)}
.newsletter{position:relative;width:1200px;height:2951px}

/* Header */
.masthead{position:absolute;left:0;top:0;width:1200px;height:270px;background:var(--white);box-shadow:0 6px 14px rgba(0,0,0,.08)}
.brand{position:absolute;left:98px;top:68px;display:flex;align-items:center;gap:14px}
.brand-dot{flex:none;width:24px;height:24px;border-radius:50%;background:var(--teal)}
.brand-name{font-family:"Montserrat",sans-serif;font-weight:600;font-size:34px;line-height:1.1;color:var(--teal);width:240px}
.browser-note{position:absolute;left:524px;top:114px;font-size:14.5px;font-weight:600;letter-spacing:.4px;color:var(--ink);white-space:nowrap}
.browser-note a{color:var(--link);text-decoration:none}
.main-nav{position:absolute;left:92px;right:82px;top:208px;display:flex;justify-content:space-between;font-weight:600;font-size:24px;color:#111}

/* Tiles */
.tile{position:absolute;overflow:hidden;border:2px solid var(--rule)}
.tile::after{content:"";position:absolute;inset:8px;border:1px solid rgba(255,255,255,.55);pointer-events:none}
.photo{position:absolute;inset:0}

/* Hero */
.hero{left:81px;top:325px;width:1040px;height:526px}
.hero .photo{background:linear-gradient(160deg,#4f4c48 0%,#7e7870 45%,#a38f6c 70%,#6c604f 100%)}
.hero-copy{position:absolute;left:600px;top:62px;width:400px;text-align:center;color:var(--white)}
.hero-rule{height:2px;background:rgba(255,255,255,.7);margin:0 110px}
.hero-title{font-weight:700;font-size:31px;letter-spacing:1px;margin-top:20px;line-height:1;white-space:nowrap}
.hero-band{position:relative;margin:12px 0 0 30px;background:var(--teal);font-size:23px;font-weight:600;letter-spacing:3px;padding:7px 0;white-space:nowrap}
.new-tag{position:absolute;left:-28px;top:-8px;background:var(--red);font-size:12px;font-weight:700;padding:4px 8px;letter-spacing:1px}
.hero-sub{font-weight:700;font-size:21px;letter-spacing:1px;line-height:1.25;margin:16px 0 14px 30px;white-space:nowrap}

/* Tailgating */
.side-bar{position:absolute;left:81px;top:863px;width:54px;height:558px;background:#4a4540}
.tailgate{left:162px;top:863px;width:539px;height:558px}
.tailgate .photo{background:linear-gradient(115deg,#f3f3f1 0%,#e8e8e6 42%,#9b9c9e 62%,#4b4c4f 100%)}
.tailgate-copy{position:absolute;left:30px;top:80px;width:390px}
.tailgate-title{font-weight:800;font-size:46px;letter-spacing:1px;line-height:1}
.tailgate-tag{display:inline-block;background:var(--slate);color:var(--white);font-weight:700;font-size:19px;letter-spacing:1px;padding:5px 12px;margin-top:8px}
.tailgate-lead{color:var(--teal);font-weight:700;font-size:25px;line-height:1.15;margin-top:14px}
.tailgate-body{font-family:"Open Sans",sans-serif;font-size:15px;line-height:1.6;color:var(--grey-text);margin-top:16px;width:300px}

/* Sale */
.sale{left:725px;top:863px;width:396px;height:268px;background:var(--white)}
.sale .photo{left:auto;width:170px;background:linear-gradient(90deg,#ffffff,#e4e4e4 40%,#b9b9b9 55%,#f3f3f3 75%)}
.sale-copy{position:absolute;left:26px;top:30px;width:210px}
.sale-title{font-weight:800;font-size:36px;line-height:1}
.red-tag{display:inline-block;background:var(--red);color:var(--white);font-weight:700;font-size:14px;letter-spacing:1px;padding:4px 8px;margin-top:6px}
.sale-line{font-weight:700;font-size:17px;line-height:1.15;color:#9a9a9a;margin-top:8px}
.sale-small{font-family:"Open Sans",sans-serif;font-size:11px;color:var(--grey-text);margin-top:4px}
.sale-copy .coupon{margin-top:30px}

/* Tabletop */
.tabletop{left:725px;top:1146px;width:396px;height:275px;background:var(--white)}
.tabletop .photo{top:60px;background:linear-gradient(135deg,#f6f1ec 0%,#e46a55 35%,#f3e7e0 55%,#d4493a 80%,#f4ece6 100%)}
.tabletop-label{position:absolute;left:22px;top:18px;font-family:"Oswald",sans-serif;font-weight:600;font-size:24px;color:var(--red);letter-spacing:.5px}

/* Bathroom accessories */
.bath{left:81px;top:1436px;width:1040px;height:236px}
.bath .photo{background:linear-gradient(90deg,#e9e7e1 0%,#d7d4cc 50%,#bdbdbd 80%,#6f6f72 100%)}
.bath-band{position:absolute;left:95px;top:59px;width:740px;height:49px;background:var(--pink);color:var(--white);text-align:center;font-family:"Raleway",sans-serif;font-weight:700;font-size:26px;letter-spacing:9px;line-height:49px}
.bath-chips{position:absolute;left:230px;top:112px;display:flex;gap:5px}
.chip{height:49px;line-height:49px;color:var(--white);font-family:"Raleway",sans-serif;font-weight:700;font-size:22px;letter-spacing:4px;text-align:center}
.chip-towel{width:224px;background:var(--mustard)}
.chip-bidet{width:358px;background:var(--teal)}

/* Authentic accents */
.accents{left:81px;top:1687px;width:509px;height:280px}
.accents .photo{background:linear-gradient(120deg,#9a9580 0%,#6d6a58 35%,#8a6a47 60%,#3e3327 100%)}
.accents-copy{position:absolute;left:0;right:0;top:108px;text-align:center;font-family:"Raleway",sans-serif;font-weight:300;color:var(--white);font-size:31px;letter-spacing:5px;line-height:1.1}

/* Garden style */
.garden-style{left:607px;top:1687px;width:514px;height:280px;background:var(--white)}
.garden-style .photo{right:auto;width:230px;background:linear-gradient(140deg,#3bb7dc 0%,#d9e7c9 45%,#7fb9a6 70%,#1d8eb0 100%)}
.garden-copy{position:absolute;left:236px;top:26px;width:262px}
.garden-title{font-weight:800;font-size:31px;line-height:1;white-space:nowrap}
.lime-tag{display:inline-block;background:var(--lime);color:var(--white);font-weight:700;font-size:17px;letter-spacing:.5px;padding:4px 10px;margin-top:6px}
.garden-body{font-family:"Open Sans",sans-serif;font-size:14.5px;line-height:1.7;color:var(--grey-text);margin-top:14px}

/* Travel */
.travel{left:81px;top:1984px;width:509px;height:352px;background:var(--white)}
.travel .photo{left:92px;background:linear-gradient(180deg,#ffffff 0%,#4a4a4c 35%,#1d1d1f 70%,#f4f4f4 100%)}
.travel-bar{position:absolute;left:0;top:0;width:92px;height:100%;background:var(--teal)}
.travel-box{position:absolute;left:12px;top:18px;width:68px;height:316px;background:#231f20}
.travel-text{position:absolute;left:46px;top:176px;transform:translate(-50%,-50%) rotate(-90deg);white-space:nowrap;font-family:"Oswald",sans-serif;font-weight:500;font-size:27px;letter-spacing:6px;color:var(--white);line-height:1.2;text-align:center}

/* Statuary */
.statuary{left:607px;top:1984px;width:514px;height:278px}
.statuary .photo{background:linear-gradient(90deg,#4f4536 0%,#6e6451 40%,#a9a99b 65%,#6f7a5f 100%)}
.statuary-copy{position:absolute;left:28px;top:72px;color:var(--white);font-family:"Raleway",sans-serif;font-weight:300;line-height:1.05;letter-spacing:1px}
.statuary-copy .small{font-size:18px}
.statuary-copy .big{font-size:32px}
.statuary-copy .mid{font-size:20px}
.lime-strip{position:absolute;left:607px;top:2280px;width:514px;height:56px;background:var(--lime)}

/* Leisure */
.leisure{left:81px;top:2353px;width:1040px;height:236px}
.leisure .photo{background:linear-gradient(100deg,#7da34a 0%,#5e7f35 35%,#c4a77b 65%,#e9ddca 100%)}
.leisure-copy{position:absolute;left:70px;top:32px;width:720px;color:var(--white)}
.leisure-title{font-family:"Raleway",sans-serif;font-weight:200;font-size:58px;letter-spacing:10px;line-height:1;white-space:nowrap}
.leisure-sub{font-weight:700;font-size:20px;letter-spacing:1px;margin-top:6px;padding-left:80px;white-space:nowrap}
.leisure-body{font-family:"Open Sans",sans-serif;font-size:16px;line-height:1.5;margin-top:8px;padding-left:100px;width:640px}

/* Footer */
.site-footer{position:absolute;left:0;top:2636px;width:1200px;height:172px;background:var(--footer-bg);text-align:center}
.footer-brand{display:inline-flex;align-items:center;gap:10px;margin-top:30px}
.footer-brand .brand-dot{width:18px;height:18px}
.footer-brand .brand-name{font-size:28px;width:auto}
.footer-about{width:940px;margin:20px auto 0;font-size:13.5px;font-weight:600;letter-spacing:.5px;line-height:1.5}
.social{position:absolute;left:447px;top:2828px;display:flex;gap:12px}
.social-btn{width:74px;height:62px;border-radius:10px;background:var(--social)}
.copyright{position:absolute;left:0;right:0;top:2912px;text-align:center;font-size:13px;font-weight:600;letter-spacing:.5px}
</style>
</head>
<body>
<div class="newsletter">

  <header class="masthead">
    <div class="brand"><span class="brand-dot"></span><span class="brand-name">Ellery Rose Fine Living</span></div>
    <p class="browser-note">HAVING TROUBLE READING THIS EMAIL? <a href="#">VIEW THIS EMAIL IN YOUR BROWSER.</a></p>
    <nav class="main-nav">
      <span>HOME</span><span>BATH &amp; SPA</span><span>LINEN</span><span>KITCHEN</span><span>GARDEN</span><span>TRAVEL</span><span>GIFTS</span><span>LEISURE</span>
    </nav>
  </header>

  <section class="tile hero">
    <div class="photo" role="img" aria-label="Teak bath caddy with soap and a potted plant resting across a wooden soaking tub"></div>
    <div class="hero-copy">
      <div class="hero-rule"></div>
      <h1 class="hero-title">INTRODUCING ZEN</h1>
      <div class="hero-band"><span class="new-tag">NEW</span>TEAK COLLECTION</div>
      <p class="hero-sub">COMPLIMENT YOUR SPA<br>OR BATH</p>
      <div class="hero-rule"></div>
    </div>
  </section>

  <div class="side-bar"></div>
  <section class="tile tailgate">
    <div class="photo" role="img" aria-label="Portable charcoal grill with a cooler bag of sausages and vegetables"></div>
    <div class="tailgate-copy">
      <h2 class="tailgate-title">TAILGATING</h2>
      <span class="tailgate-tag">SHOP ALL TAILGATING</span>
      <p class="tailgate-lead">GET THE RIGHT GRILL TO MAKE THE MOST OF THE TAILGATING SEASON.</p>
      <p class="tailgate-body">Looking for tailgating grills, tailgating accessories or tailgate tables? ElleryRose.com has all your tailgating supplies.</p>
    </div>
  </section>

  <section class="tile sale">
    <div class="photo" role="img" aria-label="Row of chrome grab bars in several lengths"></div>
    <div class="sale-copy">
      <h2 class="sale-title">10% SALE</h2>
      <span class="red-tag">DO NOT MISS</span>
      <p class="sale-line">ON ALL GRAB BARS<br>ONLY THIS MONTH</p>
      <p class="sale-small">All sizes, all styles on sale</p>
      <span class="red-tag coupon">NO COUPON NEEDED</span>
    </div>
  </section>

  <section class="tile tabletop">
    <div class="photo" role="img" aria-label="Enamel tableware set decorated with red lobsters"></div>
    <span class="tabletop-label">TABLETOP</span>
  </section>

  <section class="tile bath">
    <div class="photo" role="img" aria-label="Folded white towels beside a polished chrome towel bar"></div>
    <div class="bath-band">BATHROOM ACCESSORIES</div>
    <div class="bath-chips">
      <span class="chip chip-towel">TOWEL BARS</span>
      <span class="chip chip-bidet">BIDETS, MIRRORS</span>
    </div>
  </section>

  <section class="tile accents">
    <div class="photo" role="img" aria-label="Rustic wooden board with bread, grapes and a ceramic pitcher"></div>
    <p class="accents-copy">AUTHENTIC ACCENTS<br>FOR YOUR HOME</p>
  </section>

  <section class="tile garden-style">
    <div class="photo" role="img" aria-label="Outdoor cushion with a blue and green tropical print"></div>
    <div class="garden-copy">
      <h2 class="garden-title">GARDEN STYLE</h2>
      <span class="lime-tag">FOR A POP OF COLOR!</span>
      <p class="garden-body">Whether you're looking for dainty paisley or jungalicious tropical flora to adorn your outdoor furnishings, we've have you covered.</p>
    </div>
  </section>

  <section class="tile travel">
    <div class="travel-bar"><div class="travel-box"></div></div>
    <p class="travel-text">TRAVELING?<br>VISIT OUR SHOP</p>
    <div class="photo" role="img" aria-label="Black quilted rolling travel case with extended handle"></div>
  </section>

  <section class="tile statuary">
    <div class="photo" role="img" aria-label="Weathered stone garden sculpture among greenery"></div>
    <div class="statuary-copy">
      <span class="small">CHECK OUT </span><span class="big">GARDEN</span><br>
      <span class="big">STATUARY</span><br>
      <span class="mid">AND ACCENTS</span>
    </div>
  </section>
  <div class="lime-strip"></div>

  <section class="tile leisure">
    <div class="photo" role="img" aria-label="Picnic on the grass with a wicker basket, wine and flowers"></div>
    <div class="leisure-copy">
      <h2 class="leisure-title">LEISURE LIFE</h2>
      <p class="leisure-sub">EXPERIENCE THE GREAT OUTDOORS</p>
      <p class="leisure-body">Picnic baskets and wine bags add romance to any outdoor dining experience. Get a weekend bag or insulated beach tote and dine al fresco</p>
    </div>
  </section>

  <footer class="site-footer">
    <div class="footer-brand"><span class="brand-dot"></span><span class="brand-name">Ellery Rose Fine Living</span></div>
    <p class="footer-about">ELLERY ROSE FINE LIVING IS ALL ABOUT A RELAXED, WARM AND WELCOMING LIFESTYLE. WE HAVE HANDPICKED ITEMS THAT ENHANCE THIS LIFESTYLE AND ALLOW YOU TO LET YOUR PERSONAL STYLE SHINE THROUGH.</p>
  </footer>
  <div class="social">
    <a class="social-btn" href="#" aria-label="Social profile 1"></a>
    <a class="social-btn" href="#" aria-label="Social profile 2"></a>
    <a class="social-btn" href="#" aria-label="Social profile 3"></a>
    <a class="social-btn" href="#" aria-label="Social profile 4"></a>
  </div>
  <p class="copyright">© 2013 COPYRIGHT ELLERY ROSE ENTERPRISES &amp; ELLERY ROSE FINE LIVING. ALL RIGHTS RESERVED.</p>

</div>
</body>
</html>
```